New Food Sleeve Design for British Traditional Food Manufacture - est 1976

We are a food manufacturer of a British traditional Steamed 'Rag Pudding' this is a Lancashire traditional dish. It consists of finest cuts of beef, hand wrapped in a suet pastry. Then traditionally wrapped in a rag (muslin cloth) today we use a modern plastic version to wrap the pudding then it is steamed, to create a beautiful tasting beef pudding (which is essentially a pie or parcel).
We are looking for a design on a newly developed packaging, which is basically a sleeve with two stays at either end so the product can not slip out of the packaging.
We would like to see designs that have :
1. a picture of the cooked product on the top of the sleeve - so customers can see what they will get once cooked.
2. The bottom of the package is for the ingredients, barcode best before date - We have this in hand so please do not design anything on the bottom of the package.
3.The front with the push tap and the opposite rear can be for cooking instructions or further info - we have no preference ein this area.
4. Wording/art required:
- Picture of the cooked product (I have a photo attached that can be used for now - but we intend to upgrade this photo at a later)
- Picture of the little man - however this man can be upgraded as it is 40 years old
- Wording 'Est 1976'
- if possible a British flag & wording 'Made in Britain'
=Wording 'Thornby's Beef Pudding'
- Cooking instructions - maybe use of symbols - Oven bake, Steam, Boil in the bag, Microwave. But these could potentially go on the smaller front or rear location
- We would like a black, dark grey etc colour as the background - we feel this is currently a luxurious/quality look' at the moment.
- But we are open to other colours if you want to experiment

Info attached to help you...
- We have attached the pdf of the dimensions of the packaging
- Photo of beef pudding - happy for you to remove the chips and peas if that helps
- Link to current website - www.clothbakes.co.uk
- The little man (as mentioned happy for an upgrade) we don't need the writing along with the little man
- a few photos of how the packaging works and looks (photos of stages 1 to 6)
- a few design attached of what we like, but we are not stuck to this happy to see different ideas
Updates

Update 19th January 2023
We have lots of great designs, each with parts we like. I'd like to provide some overall feedback of the items we like from the designs submitted to date:
-The little man logo. We really like the British flag represented on the apron. We think if Pembertons field larder can be removed from this logo and keep the words 'quality with convenience', 'made in Britain ' & EST 1976. I think that would be great.
-we think the pudding on its own rather than with chips and peas looks better and gives a clear indication of what the customer is buying.
-we don't need sell by/best before/batch number on the front as this will be on the rear and on the internal packaging
-do like/need the colour chart for salt/sugar/fat etc - but currently have no preference to if it's on the top or front.
-do like the symbols for cooking, but not sure we like one we have seen yet.
-lile the idea of golden/golden orange colour text in places
-really like the slight band of colour as this could be simple changed to an alternative colour for other products with have.
Hope this helps you all

Target Market(s)

Basically anyone who has an evening meal who likes to eat meat

Industry/Entity Type

Food maufacturing

Colors

Designer to choose colors to be used in the design.

Requirements
Must have
• A picture of the product when cooked
Nice to have
• Little man, established 1976, made in Britain

```html
<!DOCTYPE html>
<html lang="en">
<head>
<meta charset="utf-8">
<title>Thornby's Beef Pudding – Sleeve Top</title>
<link href="https://fonts.googleapis.com/css2?family=Archivo+Black&family=Work+Sans:ital,wght@0,400;0,500;0,600;0,700;1,300&display=swap" rel="stylesheet">
<style>
  :root {
    --backdrop: #3a0a28;
    --sleeve: #333333;
    --gold: #f0b416;
    --white: #f2f2f2;
    --flag-blue: #2a3fb8;
    --flag-red: #e21b2c;
    --photo-light: #f5c25a;
    --photo-mid: #d97a1c;
    --photo-dark: #3a1a0c;
  }
  * { margin: 0; padding: 0; box-sizing: border-box; }
  html, body { width: 1200px; height: 1200px; overflow: hidden; }
  body {
    background: var(--backdrop);
    font-family: "Work Sans", sans-serif;
    position: relative;
  }
  .sleeve-top {
    position: absolute;
    left: 200px; top: 444px;
    width: 814px; height: 366px;
    background: var(--sleeve);
  }
  .flag { position: absolute; left: 0; top: 0; width: 131px; height: 71px; }
  .mascot-area {
    position: absolute; left: 171px; top: 68px; width: 98px; height: 79px;
    border-radius: 40% 40% 8px 8px;
    background: radial-gradient(circle at 50% 40%, #f3c230 0%, #d9a411 70%, rgba(217,164,17,0.2) 100%);
  }
  .brand-block {
    position: absolute; left: 0; width: 438px; text-align: center; white-space: nowrap;
  }
  .brand-name {
    top: 159px;
    font-family: "Archivo Black", sans-serif;
    color: var(--white);
    font-size: 43px; line-height: 38px;
    font-weight: 400;
    text-transform: uppercase;
    letter-spacing: 0.5px;
  }
  .product-line {
    top: 241px;
    color: var(--gold);
    font-weight: 700; font-size: 15.2px; line-height: 18px;
    letter-spacing: 0.3px;
  }
  .tagline {
    top: 275px;
    color: var(--white);
    font-style: italic; font-weight: 300; font-size: 18px; line-height: 24px;
    letter-spacing: 1.1px;
  }
  .origin {
    top: 315px;
    color: var(--gold);
    font-weight: 500; font-size: 11.7px; line-height: 15px;
    letter-spacing: 2.1px;
  }
  .product-photo {
    position: absolute; left: 433px; top: 0; width: 381px; height: 295px;
    background:
      radial-gradient(ellipse 32% 55% at 58% 62%, var(--photo-dark) 0%, #5a2a10 55%, rgba(90,42,16,0) 100%),
      radial-gradient(ellipse 40% 40% at 18% 30%, #fde9a0 0%, rgba(253,233,160,0) 100%),
      linear-gradient(120deg, var(--photo-light) 0%, var(--photo-mid) 55%, #b8560f 100%);
  }
  .cooking-methods {
    position: absolute; left: 433px; top: 309px; width: 381px; height: 50px;
  }
  .method {
    position: absolute; top: 0; width: 90px; margin-left: -45px;
    text-align: center; color: var(--gold);
    font-size: 7.3px; font-weight: 600; line-height: 9px;
  }
  .method svg { display: block; margin: 1px auto 3px; width: 30px; height: 19px; }
  .method-oven { left: 57px; }
  .method-microwave { left: 156px; }
  .method-steam { left: 254px; }
  .method-bag { left: 339px; }
</style>
</head>
<body>
  <section class="sleeve-top">
    <svg class="flag" viewBox="0 0 60 32" preserveAspectRatio="none" aria-label="Union flag">
      <rect width="60" height="32" fill="var(--flag-blue)"/>
      <path d="M0,0 L60,32 M60,0 L0,32" stroke="#fff" stroke-width="6"/>
      <path d="M0,0 L60,32 M60,0 L0,32" stroke="var(--flag-red)" stroke-width="2"/>
      <path d="M30,0 V32 M0,16 H60" stroke="#fff" stroke-width="10"/>
      <path d="M30,0 V32 M0,16 H60" stroke="var(--flag-red)" stroke-width="6"/>
    </svg>

    <div class="mascot-area" role="img" aria-label="Brand mascot illustration in gold"></div>

    <h1 class="brand-block brand-name">Thornby's<br>Beef Pudding</h1>
    <p class="brand-block product-line">TRADITIONAL LANCASHIRE RAG PUDDING</p>
    <p class="brand-block tagline">Quality With Convenience</p>
    <p class="brand-block origin">MADE IN BRITAIN<br>EST 1976</p>

    <div class="product-photo" role="img" aria-label="Photo of the cooked beef rag pudding opened to show beef and gravy"></div>

    <div class="cooking-methods">
      <div class="method method-oven">10-15 min
        <svg viewBox="0 0 30 19"><rect x="1" y="1" width="28" height="17" rx="1" fill="none" stroke="var(--gold)" stroke-width="1.4"/><line x1="1" y1="5" x2="29" y2="5" stroke="var(--gold)" stroke-width="1.2"/><circle cx="4.5" cy="3" r="0.9" fill="var(--gold)"/><circle cx="7.5" cy="3" r="0.9" fill="var(--gold)"/><circle cx="10.5" cy="3" r="0.9" fill="var(--gold)"/><rect x="4" y="8" width="22" height="7" fill="none" stroke="var(--gold)" stroke-width="1.2"/></svg>
        Oven Baked</div>
      <div class="method method-microwave">15-25 min
        <svg viewBox="0 0 30 19"><rect x="1" y="1" width="28" height="16" rx="1" fill="none" stroke="var(--gold)" stroke-width="1.4"/><rect x="3.5" y="4" width="17" height="10" rx="1" fill="none" stroke="var(--gold)" stroke-width="1.2"/><line x1="23" y1="3" x2="23" y2="15" stroke="var(--gold)" stroke-width="1"/><circle cx="26" cy="6" r="1" fill="var(--gold)"/><circle cx="26" cy="11" r="1" fill="var(--gold)"/></svg>
        Microwave Baked</div>
      <div class="method method-steam">10 min
        <svg viewBox="0 0 30 19"><path d="M9,10 a3.5,3.5 0 0 1 1-6.5 a4.5,4.5 0 0 1 8.5,0 a3.5,3.5 0 0 1 1.5,6.5 Z" fill="none" stroke="var(--gold)" stroke-width="1.3"/><path d="M12,11 q-2,3 0,6 M15,11 q-2,3 0,6 M18,11 q-2,3 0,6" fill="none" stroke="var(--gold)" stroke-width="1.1"/></svg>
        Steam Boiled</div>
      <div class="method method-bag">15 min
        <svg viewBox="0 0 30 19"><rect x="12" y="1" width="6" height="3" rx="1" fill="var(--gold)"/><path d="M12,5 H18 L23,14 Q23,18 19,18 H11 Q7,18 7,14 Z" fill="var(--gold)"/></svg>
        Bag Boiled</div>
    </div>
  </section>
</body>
</html>
```